Plovenworks business card

We need a modern business card - With our 4 colors - See web: www.plovenworks.dk

I have attached logo and som old business Cards we have - Lets Make the new ones shine...:-) -

Industry/Entity Type

Business

Requirements
Must have
• the logo with plovnworks only,

```html
<!DOCTYPE html>
<html lang="da">
<head>
<meta charset="utf-8">
<title>Plovenworks – visitkort</title>
<link rel="stylesheet" href="https://fonts.googleapis.com/css2?family=Josefin+Sans:wght@300;400;600&display=swap">
<style>
  :root {
    --backdrop: #e7e4df;
    --paper: #f4f4f4;
    --charcoal: #3d3d3d;
    --ink: #555555;
    --magenta: #c8318a;
    --lime: #8cc63f;
    --orange: #e8842c;
    --purple: #6d2a7a;
  }
  * { box-sizing: border-box; margin: 0; padding: 0; }
  html, body { width: 1200px; height: 1023px; overflow: hidden; }
  body {
    background: var(--backdrop);
    font-family: "Josefin Sans", sans-serif;
    position: relative;
  }
  .card {
    position: absolute;
    left: 250px;
    width: 700px;
    height: 400px;
    box-shadow: 0 6px 18px rgba(0,0,0,.18);
    overflow: hidden;
  }
  .card--front { top: 90px; background: var(--paper); }
  .card--back { top: 540px; background: var(--charcoal); }

  /* front: identity block */
  .identity { position: absolute; left: 60px; top: 120px; width: 290px; }
  .brand { display: flex; align-items: center; gap: 14px; }
  .brand__dot {
    width: 34px; height: 34px; border-radius: 50%;
    background: var(--lime);
  }
  .brand__name {
    font-size: 38px; font-weight: 300; color: var(--orange);
    letter-spacing: 1px;
  }
  .identity__rule {
    height: 3px; background: var(--lime); margin: 12px 0 14px;
  }
  .identity__name { font-size: 36px; font-weight: 300; color: var(--ink); }
  .identity__title {
    font-size: 24px; font-weight: 400; color: var(--magenta); margin-top: 8px;
  }

  /* front: contact timeline */
  .timeline {
    position: absolute; left: 410px; top: 0; width: 6px; height: 400px;
    background: linear-gradient(var(--magenta) 0 42%, var(--lime) 42% 68%, var(--orange) 68% 90%, var(--purple) 90% 100%);
  }
  .contact {
    position: absolute; left: 390px; display: flex; align-items: center; gap: 22px;
  }
  .contact__icon {
    width: 46px; height: 46px; border-radius: 50%;
    display: flex; align-items: center; justify-content: center;
    box-shadow: 0 2px 4px rgba(0,0,0,.25);
  }
  .contact__icon svg { width: 24px; height: 24px; fill: var(--charcoal); }
  .contact__icon--pin { background: var(--magenta); }
  .contact__icon--phone { background: var(--lime); }
  .contact__icon--mail { background: var(--orange); }
  .contact__lines { font-size: 21px; font-weight: 300; color: var(--ink); line-height: 1.45; letter-spacing: .5px; }
  .contact--address { top: 78px; }
  .contact--phone { top: 178px; }
  .contact--mail { top: 278px; }

  /* back */
  .band { position: absolute; height: 46px; }
  .band--purple { left: 0; top: 0; width: 110px; background: var(--purple); }
  .band--lime { left: 110px; top: 0; width: 90px; background: var(--lime); }
  .band--orange { right: 90px; bottom: 0; width: 110px; background: var(--orange); }
  .band--magenta { right: 0; bottom: 0; width: 90px; background: var(--magenta); }
</style>
</head>
<body>
  <section class="card card--front" aria-label="Visitkort forside">
    <div class="identity">
      <div class="brand">
        <span class="brand__dot"></span>
        <span class="brand__name">plovnworks</span>
      </div>
      <div class="identity__rule"></div>
      <p class="identity__name">Jonas Vedelholm</p>
      <p class="identity__title">Salgsdirektor</p>
    </div>

    <div class="timeline"></div>

    <div class="contact contact--address">
      <span class="contact__icon contact__icon--pin">
        <svg viewBox="0 0 24 24"><path d="M12 2a7 7 0 0 0-7 7c0 5 7 13 7 13s7-8 7-13a7 7 0 0 0-7-7zm0 9.5A2.5 2.5 0 1 1 12 6.5a2.5 2.5 0 0 1 0 5z"/></svg>
      </span>
      <p class="contact__lines">Kastanievej 14<br>2000 Frederiksberg</p>
    </div>

    <div class="contact contact--phone">
      <span class="contact__icon contact__icon--phone">
        <svg viewBox="0 0 24 24"><path d="M6.6 10.8a15.1 15.1 0 0 0 6.6 6.6l2.2-2.2a1 1 0 0 1 1-.25 11.4 11.4 0 0 0 3.6.57 1 1 0 0 1 1 1V20a1 1 0 0 1-1 1A17 17 0 0 1 3 4a1 1 0 0 1 1-1h3.5a1 1 0 0 1 1 1c0 1.25.2 2.45.57 3.6a1 1 0 0 1-.25 1z"/></svg>
      </span>
      <p class="contact__lines">+45 31 42 67 80<br>+45 52 19 48 03</p>
    </div>

    <div class="contact contact--mail">
      <span class="contact__icon contact__icon--mail">
        <svg viewBox="0 0 24 24"><path d="M3 5h18v14H3zm2 2v.5l7 5 7-5V7zm0 3v7h14v-7l-7 5z"/></svg>
      </span>
      <p class="contact__lines">jv@plovenworks.dk<br>info@plovenworks.dk</p>
    </div>
  </section>

  <section class="card card--back" aria-label="Visitkort bagside">
    <span class="band band--purple"></span>
    <span class="band band--lime"></span>
    <span class="band band--orange"></span>
    <span class="band band--magenta"></span>
  </section>
</body>
</html>
```